KAV cards & more
Business cards, fax cover sheet, letterhead, envelopes, powerpoint slide template
Modern
Tad Willers
Owner
17 Lindgate Row Bedminster, NJ 07921
twkav@mailvane.net
Please integrate my already-completed company logo (attached) in a clean, modern design for business cards, Fax cover sheet, letterhead, envelopes, and powerpoint slide template

```html
<!DOCTYPE html>
<html lang="en">
<head>
<meta charset="utf-8">
<title>KAV Stationery Set</title>
<link href="https://fonts.googleapis.com/css2?family=Montserrat:wght@400;600;700&family=Open+Sans:wght@400;600&display=swap" rel="stylesheet">
<style>
  :root{
    --green:#2e9b3a;
    --green-dark:#1e7a2b;
    --green-light:#8cc63f;
    --paper:#ffffff;
    --stage:#e4e6e4;
    --ink:#3a3a3a;
    --muted:#8a8f8a;
    --rule:#d4d8d4;
  }
  *{box-sizing:border-box;margin:0;padding:0}
  html,body{width:1200px;height:871px;overflow:hidden}
  body{background:var(--stage);font-family:"Open Sans",Arial,sans-serif;color:var(--ink);position:relative}
  .sheet{position:absolute;background:var(--paper);box-shadow:0 3px 10px rgba(0,0,0,.18);overflow:hidden}
  .brand{display:flex;align-items:center;gap:6px;font-family:"Montserrat",Arial,sans-serif;font-weight:700;color:var(--green);letter-spacing:1px}
  .brand .dot{border-radius:50%;background:var(--green)}
  .brand.small{font-size:16px}.brand.small .dot{width:14px;height:14px}
  .tiny{font-size:6.5px;line-height:1.5;color:var(--muted)}

  /* letterhead */
  .letterhead{left:40px;top:36px;width:300px;height:424px;padding:22px 24px}
  .letterhead .head-rule{height:2px;background:linear-gradient(90deg,var(--green),var(--green-light));margin:10px 0 22px}
  .letterhead .body p{font-size:6.5px;line-height:1.6;color:#666;margin-bottom:8px}
  .letterhead .sign{margin-top:18px;font-size:7px;color:var(--ink)}
  .letterhead .foot{position:absolute;left:0;right:0;bottom:0;height:34px;background:linear-gradient(90deg,var(--green-dark),var(--green-light));color:#fff;font-size:6.5px;display:flex;align-items:center;justify-content:center;gap:14px}

  /* fax */
  .fax{left:370px;top:36px;width:300px;height:424px;padding:22px 24px}
  .fax .top{display:flex;justify-content:space-between;align-items:center;border-bottom:2px solid var(--green);padding-bottom:8px}
  .fax h1{font-family:"Montserrat",Arial,sans-serif;font-size:22px;font-weight:700;color:var(--ink);letter-spacing:2px}
  .fax table{width:100%;border-collapse:collapse;margin-top:14px;font-size:7px}
  .fax td{padding:6px 4px;border-bottom:1px solid var(--rule)}
  .fax td.label{width:22%;color:var(--green-dark);font-weight:600;background:#f1f6ef}
  .fax .checks{display:flex;flex-wrap:wrap;gap:6px 12px;margin:14px 0;font-size:6.5px}
  .fax .checks span::before{content:"";display:inline-block;width:7px;height:7px;border:1px solid var(--muted);margin-right:3px;vertical-align:-1px}
  .fax .comments{font-size:7px;font-weight:600;color:var(--green-dark);margin-bottom:6px}
  .fax .line{height:1px;background:var(--rule);margin:13px 0}

  /* slides */
  .slide{left:700px;width:460px;height:259px}
  .slide.title{top:36px}
  .slide.content{top:320px;padding:22px 26px}
  .slide svg.swoosh{position:absolute;left:0;top:0}
  .slide.title .brand{position:absolute;left:26px;top:24px}
  .slide.title h2{position:absolute;left:120px;top:150px;font-family:"Montserrat",Arial,sans-serif;font-weight:600;font-size:22px;color:#fff}
  .slide.content .bar{position:absolute;left:0;right:0;bottom:0;height:14px;background:linear-gradient(90deg,var(--green-dark),var(--green-light))}
  .slide.content .cols{display:flex;gap:26px;margin-top:18px}
  .slide.content .col{flex:1}
  .slide.content h3{font-family:"Montserrat",Arial,sans-serif;font-size:11px;color:var(--ink);margin-bottom:6px}
  .slide.content .frame{height:66px;border:2px solid var(--green);margin-bottom:8px}

  /* envelope */
  .envelope{left:40px;top:500px;width:460px;height:230px;padding:20px 24px}
  .envelope .addr{margin-top:6px}
  .envelope .band{position:absolute;left:0;top:0;bottom:0;width:10px;background:linear-gradient(180deg,var(--green-light),var(--green-dark))}
  .envelope .foot{position:absolute;left:24px;right:24px;bottom:14px;border-top:1px solid var(--rule);padding-top:6px}

  /* cards */
  .card{width:250px;height:144px}
  .card.front{left:540px;top:610px;padding:18px 18px}
  .card.front .name{font-family:"Montserrat",Arial,sans-serif;font-weight:600;font-size:11px;margin-top:20px;color:var(--ink)}
  .card.front .role{font-size:7px;color:var(--green);margin-bottom:8px}
  .card.front .edge{position:absolute;right:0;top:0;bottom:0;width:8px;background:var(--green)}
  .card.back{left:820px;top:610px;background:linear-gradient(135deg,var(--green-light),var(--green-dark));display:flex;align-items:center;justify-content:center}
  .card.back .brand{color:#fff;font-size:26px}
  .card.back .brand .dot{background:#fff;width:22px;height:22px}
</style>
</head>
<body>

<section class="sheet letterhead">
  <div class="brand small"><span class="dot"></span>KAV</div>
  <div class="head-rule"></div>
  <div class="body">
    <p>June 12, 2024<br>Mr. Carl Benton<br>220 Market Street<br>Summit, NJ 07901</p>
    <p>Dear Mr. Benton,</p>
    <p>Thank you for your recent inquiry. We are pleased to share our full range of services and look forward to working with you on your upcoming project this season.</p>
    <p>Our team will prepare a detailed proposal outlining scope, timing and costs. Please do not hesitate to contact us with any questions in the meantime.</p>
    <p>We value your trust and hope to build a lasting partnership.</p>
    <div class="sign">Sincerely,<br><br>Tad Willers<br><span class="tiny">Owner</span></div>
  </div>
  <div class="foot"><span>17 Lindgate Row Bedminster, NJ 07921</span><span>twkav@mailvane.net</span></div>
</section>

<section class="sheet fax">
  <div class="top"><div class="brand small"><span class="dot"></span>KAV</div><h1>FAX</h1></div>
  <table>
    <tr><td class="label">To:</td><td></td><td class="label">From:</td><td></td></tr>
    <tr><td class="label">Fax:</td><td></td><td class="label">Pages:</td><td></td></tr>
    <tr><td class="label">Phone:</td><td></td><td class="label">Date:</td><td></td></tr>
    <tr><td class="label">Re:</td><td></td><td class="label">CC:</td><td></td></tr>
  </table>
  <div class="checks"><span>Urgent</span><span>For Review</span><span>Please Comment</span><span>Please Reply</span></div>
  <div class="comments">Comments:</div>
  <div class="line"></div><div class="line"></div><div class="line"></div><div class="line"></div><div class="line"></div><div class="line"></div><div class="line"></div>
</section>

<section class="sheet slide title">
  <svg class="swoosh" width="460" height="259" viewBox="0 0 460 259" aria-hidden="true">
    <path d="M0 259 L0 170 C140 150 300 110 460 20 L460 259 Z" fill="#1e7a2b"/>
    <path d="M0 259 L0 190 C150 170 310 130 460 50 L460 259 Z" fill="#2e9b3a"/>
    <path d="M0 259 L0 210 C160 195 320 165 460 100 L460 259 Z" fill="#8cc63f"/>
  </svg>
  <div class="brand small"><span class="dot"></span>KAV</div>
  <h2>The Presentation Title</h2>
</section>

<section class="sheet slide content">
  <div class="brand small"><span class="dot"></span>KAV</div>
  <div class="cols">
    <div class="col"><h3>Title</h3><div class="frame"></div><p class="tiny">Short supporting text describes this point clearly for the audience here.</p></div>
    <div class="col"><h3>Title</h3><div class="frame"></div><p class="tiny">Short supporting text describes this point clearly for the audience here.</p></div>
  </div>
  <div class="bar"></div>
</section>

<section class="sheet envelope">
  <div class="band"></div>
  <div class="brand small"><span class="dot"></span>KAV</div>
  <div class="addr tiny">17 Lindgate Row<br>Bedminster, NJ 07921</div>
  <div class="foot tiny">twkav@mailvane.net &nbsp;|&nbsp; www.hukav.com &nbsp;|&nbsp; (555) 014-2290</div>
</section>

<section class="sheet card front">
  <div class="brand small"><span class="dot"></span>KAV</div>
  <div class="name">Tad Willers</div>
  <div class="role">Owner</div>
  <div class="tiny">17 Lindgate Row Bedminster, NJ 07921<br>twkav@mailvane.net<br>(555) 014-2290</div>
  <div class="edge"></div>
</section>

<section class="sheet card back">
  <div class="brand"><span class="dot"></span>KAV</div>
</section>

</body>
</html>
```